IT business looking for Standout Letterhead Design

We need a letterhead design for a company based in Harborview, CA called Corvane Systems, Inc. We specialize in IT engineering, installation and technical support pertaining to the department of defense.

We would like to see a design that incorporates the black and gold that matches our company logo.

More information on the company can be found at www.corvane-sys.example

```html
<!DOCTYPE html>
<html lang="en">
<head>
<meta charset="utf-8">
<title>Corvane Systems, Inc. — Letterhead</title>
<link rel="stylesheet" href="https://fonts.googleapis.com/css2?family=Cinzel:wght@500&family=Open+Sans:wght@700&display=swap">
<style>
  :root {
    --ink: #111111;
    --gold: #f2d500;
    --gold-deep: #c9a227;
    --cream: #f6f1c6;
    --cream-light: #fbf9e6;
    --paper: #ffffff;
    --paper-shade: #e4e4e4;
    --text: #1e1e1e;
  }
  html, body {
    margin: 0;
    padding: 0;
    overflow: hidden;
    background: #ffffff;
  }
  .letterhead {
    position: relative;
    width: 877px;
    height: 1200px;
    overflow: hidden;
    background: linear-gradient(180deg, var(--cream) 0%, var(--cream-light) 20%, var(--cream-light) 80%, var(--cream) 100%);
  }
  .letterhead__art {
    position: absolute;
    inset: 0;
    width: 877px;
    height: 1200px;
  }
  .brand {
    position: absolute;
    left: 36px;
    top: 40px;
    width: 184px;
    text-align: center;
    color: var(--ink);
    font-family: "Cinzel", serif;
    font-weight: 500;
  }
  .brand__dot {
    display: block;
    width: 52px;
    height: 52px;
    margin: 0 auto 14px;
    border-radius: 50%;
    background: var(--gold-deep);
  }
  .brand__name {
    display: block;
    font-size: 38px;
    line-height: 1;
    letter-spacing: 1px;
  }
  .brand__tagline {
    display: block;
    margin-top: 6px;
    font-size: 11px;
    letter-spacing: 1px;
  }
  .emblem-area {
    position: absolute;
    left: 80px;
    top: 330px;
    width: 780px;
    height: 640px;
    border-radius: 50%;
    background: radial-gradient(closest-side, rgba(200,200,200,0.35), rgba(200,200,200,0));
  }
  .contacts {
    position: absolute;
    left: 44px;
    top: 1067px;
    margin: 0;
    padding: 0;
    list-style: none;
    font-family: "Open Sans", sans-serif;
    font-weight: 700;
    font-size: 14.5px;
    color: var(--text);
  }
  .contacts__item {
    display: flex;
    align-items: center;
    height: 28px;
  }
  .contacts__icon {
    width: 16px;
    height: 16px;
    margin-right: 14px;
    fill: var(--ink);
  }
</style>
</head>
<body>
<main class="letterhead">
  <svg class="letterhead__art" viewBox="0 0 877 1200" aria-hidden="true">
    <defs>
      <linearGradient id="paperGradient" x1="0" y1="0" x2="0" y2="1">
        <stop offset="0" stop-color="var(--paper)"/>
        <stop offset="0.55" stop-color="#f2f2f2"/>
        <stop offset="1" stop-color="var(--paper-shade)"/>
      </linearGradient>
    </defs>
    <!-- writing area -->
    <path d="M0 256 C300 182 600 140 877 148 L877 1086 C600 1066 300 1010 0 1000 Z" fill="url(#paperGradient)"/>
    <!-- top gold ribbon -->
    <path d="M0 196 C160 188 320 172 500 150 C320 180 160 202 0 226 Z" fill="var(--gold)"/>
    <!-- top black swoosh -->
    <path d="M0 232 C300 160 600 118 877 122 L877 146 C600 140 300 182 0 256 Z" fill="var(--ink)"/>
    <!-- top right gold accent -->
    <path d="M420 176 C600 148 760 144 877 150 L877 162 C760 158 600 160 420 176 Z" fill="var(--gold)"/>
    <!-- bottom gold ribbon left -->
    <path d="M0 1010 C200 1016 360 1034 520 1060 C360 1048 200 1036 0 1028 Z" fill="var(--gold)" opacity="0.75"/>
    <!-- bottom black swoosh -->
    <path d="M0 982 C300 992 600 1050 877 1080 L877 1104 C600 1082 300 1018 0 1006 Z" fill="var(--ink)"/>
    <!-- bottom right gold accent -->
    <path d="M480 1084 C650 1098 775 1104 877 1104 L877 1114 C775 1114 650 1108 480 1084 Z" fill="var(--gold)"/>
  </svg>

  <div class="emblem-area" role="img" aria-label="Faint company emblem watermark area"></div>

  <header class="brand">
    <span class="brand__dot"></span>
    <span class="brand__name">CORVANE</span>
    <span class="brand__tagline">SYSTEMS, INC.</span>
  </header>

  <ul class="contacts">
    <li class="contacts__item">
      <svg class="contacts__icon" viewBox="0 0 16 16" aria-hidden="true"><path d="M8 0C4.8 0 2.5 2.4 2.5 5.4 2.5 9.4 8 16 8 16s5.5-6.6 5.5-10.6C13.5 2.4 11.2 0 8 0zm0 7.6a2.3 2.3 0 1 1 0-4.6 2.3 2.3 0 0 1 0 4.6z"/></svg>
      Harborview, CA
    </li>
    <li class="contacts__item">
      <svg class="contacts__icon" viewBox="0 0 16 16" aria-hidden="true"><path d="M3.4 0.6l2.3 3.3-1.4 1.6c.9 2.2 2.6 4 4.8 5l1.6-1.4 3.3 2.3-1.1 3.2C7 14.4 1.4 8.8 0.3 1.7z"/></svg>
      619-555-0142 / 619-555-0187
    </li>
    <li class="contacts__item">
      <svg class="contacts__icon" viewBox="0 0 16 16" aria-hidden="true"><path d="M0 3h16v1.2L8 9 0 4.2zM0 5.8l8 4.8 8-4.8V13H0z"/></svg>
      info@corvane-sys.example
    </li>
    <li class="contacts__item">
      <svg class="contacts__icon" viewBox="0 0 16 16" aria-hidden="true"><path d="M8 0a8 8 0 1 0 0 16A8 8 0 0 0 8 0zm5.9 7.2h-2.6a12 12 0 0 0-1.1-5.1 6.5 6.5 0 0 1 3.7 5.1zM8 1.5c.8 1 1.6 3 1.8 5.7H6.2C6.4 4.5 7.2 2.5 8 1.5zM5.8 2.1a12 12 0 0 0-1.100 5.1H2.1a6.5 6.5 0 0 1 3.7-5.1zM2.1 8.8h2.6c.1 2 .5 3.7 1.1 5.1a6.5 6.5 0 0 1-3.7-5.1zM8 14.5c-.8-1-1.6-3-1.8-5.7h3.6c-.2 2.7-1 4.7-1.8 5.7zm2.2-.6c.6-1.4 1-3.1 1.1-5.1h2.6a6.5 6.5 0 0 1-3.7 5.1z"/></svg>
      www.corvane-sys.example
    </li>
  </ul>
</main>
</body>
</html>
```